E-Book-Cover für Ratgeber zum Thema Weisheit
Der Designer "pinselwerk" hat das Kunststück vollbracht, schon mit seinem ersten Entwurf genau ins Schwarze zu treffen, sodass nur noch Feinheiten abgestimmt werden mussten. Nach kleinen Wartezeiten ging er auf meine Wünsche ein und lieferte ein optimales Ergebnis ab, ohne dabei viele Worte zu verlieren. Er übermittelte mir eine farbige und eine schwarzweiße Variante des Designs in verschiedenen Dateiformaten. Ich kann diesen Designer nur empfehlen und würde wieder mit ihm arbeiten.
Zielgruppe
Ich bin ein experimenteller Schriftsteller, der ein E-Book über Lumora Self Press auf Varnello veröffentlichen möchte. Das Thema des Ratgebers ist Weisheit.
Weisheit gilt als ein eher antiquierter und abstrakter Begriff. Das ist ein Irrtum. Sie ist wichtiger als je zuvor und kann beschrieben werden. Weder ist sie gleichzusetzen mit Klugheit, noch mit spiritueller Erleuchtung. Sie beinhaltet bestimmte Eigenschaften wie Vernunft, Wissbegierde, Demut, Einfühlungsvermögen, Intuition, Auflehnung... Wobei rationales Denken das oberste Gebot ist. Es wird u.a. gezeigt, was Weisheit für das eigene Leben bringt und wie man sie anstreben kann.
Die Zielgruppe sind alle Menschen, die an Philosophie, Psychologie, Selbstoptimierung oder Religionen bzw. Atheismus interessiert sind. Menschen, die nach einer Erkenntnis oder 'Erleuchtung' suchen und etwas Besonderes in der Bücherflut entdecken möchten. Es ist weniger für Akademiker geschrieben; eher für die 'normale', durchschnittliche Bevölkerung und kann auch von bildungsferneren Schichten aller Altersgruppen verstanden werden.
Meine Vermutung ist, dass es bei offenen Personen mittleren Alters Anklang finden könnte.
Aufgabenstellung
Der Titel und der Untertitel des Buches müssen vorkommen (Titel: 'Das Stille Feuer'; Untertitel: 'Wie Sie durch einen kühnen Ansatz des klaren Handelns echte Stärke gewinnen'). Außerdem soll ein runder Button/Aufkleber/Sticker auf dem Cover kleben, welcher folgenden Text enthält: 'Mit Selbsttest! Wie weise bin ich?').
Natürlich soll der Name des Autors ebenfalls vorkommen: 'Till Brauner'
Das Cover soll sehr aus der Masse herausstechen, demnach ein echter Hingucker sein. Der potenzielle Kunde soll sofort neugierig sein! Es muss sowohl klein (als Thumbnail und am Smartphone), als auch groß gut aussehen und der Titel stets gut lesbar sein. Außerdem muss es schwarzweiß gut aussehen und erkennbar sein (für ebook-reader).
Varnello gibt folgende Werte für die Bilddatei vor: Die idealen Abmessungen für Coverdateien liegen bei 2 560 x 1 600 Pixeln. Mindestens 300 dpi. Die Größe der Bilddatei sollte 50MB nicht übersteigen. Farbprofil: RGB. DATEIFORMAT: JPG oder TIFF
Coverbilder mit weißem oder sehr hellem Hintergrund heben sich kaum vom Hintergrund ab. Fügen Sie einen dünnen Rahmen (3–4 Pixel) in Mittelgrau hinzu, um die Ränder des Coverbilds besser sichtbar zu machen.
Welches Cover gut zum Thema Weisheit passt, überlasse ich Ihrer Genialität. Ich dachte vielleicht an eine Art Blitz, Supernova, Erleuchtung, Explosion, geometrische Form o.ä. Aber Sie können sich etwas ganz eigenes ausdenken. Es sollte eher abstrakt sein. Außerdem muss es klar, edel und modern wirken, weniger comichaft oder verspielt/kitschig. Es darf etwas aggressiv bzw. 'revolutionär' wirken.

```html
<!DOCTYPE html>
<html lang="de">
<head>
<meta charset="utf-8">
<title>Das Stille Feuer – Till Brauner</title>
<link rel="stylesheet" href="https://fonts.googleapis.com/css2?family=Anton&family=Open+Sans:ital,wght@0,400;0,600;1,700&display=swap">
<style>
  :root {
    --paper: #eae9ea;
    --ink: #0b0b0b;
    --sticker: #0b8fc9;
    --sticker-text: #ffffff;
    --glow-core: #ffffff;
    --glow-blue: #3aa6ff;
    --glow-deep: #1b2f86;
    --head-dark: #222222;
  }
  html, body {
    margin: 0;
    padding: 0;
    overflow: hidden;
    background: var(--paper);
  }
  .cover {
    position: relative;
    width: 750px;
    height: 1200px;
    overflow: hidden;
    background: var(--paper);
  }
  .cover svg { display: block; }
  .author-name {
    font-family: "Anton", "Oswald", sans-serif;
    fill: var(--ink);
  }
  .book-title {
    font-family: "Anton", "Oswald", sans-serif;
    fill: var(--ink);
  }
  .subtitle {
    font-family: "Open Sans", Arial, sans-serif;
    font-weight: 400;
    fill: var(--ink);
  }
  .sticker-disc { fill: var(--sticker); }
  .sticker-text {
    font-family: "Open Sans", Arial, sans-serif;
    fill: var(--sticker-text);
  }
  .sticker-kicker { font-weight: 600; }
  .sticker-question { font-weight: 700; font-style: italic; }
</style>
</head>
<body>
<main class="cover">
  <svg width="750" height="1200" viewBox="0 0 750 1200" xmlns="http://www.w3.org/2000/svg">
    <defs>
      <radialGradient id="burst-glow" cx="0.47" cy="0.42" r="0.62">
        <stop offset="0" stop-color="var(--glow-core)"/>
        <stop offset="0.12" stop-color="var(--glow-blue)"/>
        <stop offset="0.42" stop-color="var(--glow-deep)"/>
        <stop offset="0.7" stop-color="var(--head-dark)" stop-opacity="0.55"/>
        <stop offset="1" stop-color="var(--paper)" stop-opacity="0"/>
      </radialGradient>
    </defs>

    <text class="author-name" x="372" y="70" font-size="50" text-anchor="middle"
          textLength="160" lengthAdjust="spacingAndGlyphs">TILL BRAUNER</text>

    <text class="book-title" x="385" y="245" font-size="182" text-anchor="middle"
          textLength="633" lengthAdjust="spacingAndGlyphs">DAS STILLE FEUER</text>

    <rect class="cover-artwork" x="15" y="250" width="720" height="810"
          fill="url(#burst-glow)" role="img"
          aria-label="Abstrakte Illustration: dunkle Kopfsilhouette im Profil mit verknäuelter weißer Linie, aus der ein blau leuchtender Lichtstrahl in eine Explosion aus Glassplittern aufsteigt"/>

    <g class="sticker" transform="rotate(8 641 677)">
      <circle class="sticker-disc" cx="641" cy="677" r="88"/>
      <text class="sticker-text sticker-kicker" x="641" y="626" font-size="21" text-anchor="middle">Mit</text>
      <text class="sticker-text sticker-kicker" x="641" y="654" font-size="21" text-anchor="middle">Selbsttest!</text>
      <text class="sticker-text sticker-question" x="639" y="694" font-size="29" text-anchor="middle">“Wie weise</text>
      <text class="sticker-text sticker-question" x="637" y="729" font-size="29" text-anchor="middle">bin ich?”</text>
    </g>

    <g class="subtitle-block">
      <text class="subtitle" x="385" y="1100" font-size="33" text-anchor="middle">WIE SIE DURCH EINEN KÜHNEN ANSATZ</text>
      <text class="subtitle" x="389" y="1143" font-size="33" text-anchor="middle">DES KLAREN HANDELNS</text>
      <text class="subtitle" x="389" y="1185" font-size="33" text-anchor="middle">ECHTE STÄRKE GEWINNEN</text>
    </g>
  </svg>
</main>
</body>
</html>
```